Business card design for web travel company

Hi
we'd like to receive some proposal for a business card design.
Stayvano is a private travel club, dedicated to all travel lovers, with unique offers for exclusive destinations all around the world. At Stayvano you can find a wide range of offers for resorts, boutique hotels and travel packages at the best guaranteed price available on the market. The convenience of the offer is guaranteed by a private sales model: offers are available for a limited time only and they are personally chosen by Stayvano's qualified team of travel experts.
We offer only exclusive hotels with discounted prices but we are not an outlet or a discount supermarket: the design should reflect our connection with luxury, exclusivity using the same style of our website www.stayvano-example.com.
We want to make sure that when we'll present ourself to our business partner they will feel immediately which is our brand positioning giving them also a sense of an affordable and reliable partner.
In attachment you can also find our brand guidelines (please note that we are NOT USING ANY MORE THE TAG LINE "Five star outlet" mentioned in it).
The info to be inserted are:
Name Surname
Job Title
Tel
Mobile (when needed)
Email
Stayvano S.r.l.
Via Bruno Lesta 27
20131 Milano

```html
<!DOCTYPE html>
<html lang="en">
<head>
<meta charset="utf-8">
<title>Stayvano – Business Card</title>
<link rel="stylesheet" href="https://fonts.googleapis.com/css2?family=Rubik:wght@300;400;500&display=swap">
<style>
  :root {
    --stage: #ece8e4;
    --card-white: #ffffff;
    --card-black: #0c0c0c;
    --ink: #1c1c1c;
    --muted: #5a5a5a;
    --gold: #b8a77a;
    --url-grey: #d6d6d6;
    --edge: #3a3a3a;
  }
  html, body {
    margin: 0;
    width: 1200px;
    height: 900px;
    overflow: hidden;
    background: var(--stage);
    font-family: "Rubik", Arial, sans-serif;
  }
  .stage {
    position: relative;
    width: 1200px;
    height: 900px;
  }
  .card {
    position: absolute;
    top: 201px;
    width: 286px;
    height: 499px;
    border-radius: 12px;
    box-sizing: border-box;
    overflow: hidden;
  }
  .card--front {
    left: 291px;
    background: var(--card-white);
    border: 1px solid var(--edge);
  }
  .card--back {
    left: 626px;
    background: var(--card-black);
  }
  .wordmark {
    margin: 0;
    font-weight: 300;
    letter-spacing: 0.5px;
    line-height: 1;
  }
  .card--front .wordmark {
    position: absolute;
    left: 20px;
    top: 26px;
    font-size: 47px;
    color: var(--ink);
  }
  .contact {
    position: absolute;
    left: 32px;
    right: 20px;
    bottom: 22px;
  }
  .contact__name {
    margin: 0;
    font-size: 21px;
    font-weight: 500;
    line-height: 26px;
    color: var(--ink);
  }
  .contact__surname { color: var(--gold); }
  .contact__title {
    margin: 0 0 10px;
    font-size: 12.5px;
    font-weight: 300;
    line-height: 18px;
    color: var(--muted);
  }
  .contact__group { margin: 0 0 8px; }
  .contact__group:last-child { margin-bottom: 0; }
  .contact__line {
    margin: 0;
    font-size: 12.5px;
    font-weight: 400;
    line-height: 17px;
    color: var(--ink);
  }
  .contact__company { font-weight: 500; }
  .back-texture {
    position: absolute;
    inset: 0;
    background: linear-gradient(135deg, #0e0e0e 0%, #1c1c1c 50%, #0e0e0e 100%);
  }
  .back-brand {
    position: absolute;
    left: 0;
    right: 0;
    top: 178px;
    text-align: center;
  }
  .card--back .wordmark {
    font-size: 46px;
    color: #ffffff;
  }
  .back-brand__url {
    margin: 12px 0 0;
    font-size: 14.5px;
    font-weight: 300;
    color: var(--url-grey);
    letter-spacing: 0.3px;
  }
</style>
</head>
<body>
<main class="stage">
  <section class="card card--front" aria-label="Business card front">
    <h1 class="wordmark">Stayvano</h1>
    <div class="contact">
      <p class="contact__name">Marco <span class="contact__surname">Dellavalle</span></p>
      <p class="contact__title">Partnership Manager</p>
      <div class="contact__group">
        <p class="contact__line">P : +00 5550 1987</p>
        <p class="contact__line">E : marco@stayvano-example.com</p>
      </div>
      <div class="contact__group">
        <p class="contact__line contact__company">Stayvano S.r.l.</p>
        <p class="contact__line">Via Bruno Lesta 27</p>
        <p class="contact__line">20131 Milano</p>
      </div>
    </div>
  </section>

  <section class="card card--back" aria-label="Business card back">
    <div class="back-texture" role="img" aria-label="Black background with fine grey diagonal stripe pattern"></div>
    <div class="back-brand">
      <p class="wordmark">Stayvano</p>
      <p class="back-brand__url">www.stayvano-example.com</p>
    </div>
  </section>
</main>
</body>
</html>
```